Buchcover-Design für Drama/Thriller/Krimi
Zielgruppe
Wir sind eine Publikation und suchen aktuell eine Design für ein Cover eines Drama-Thriller-Krimi Buches.
Zielgruppe sind alle Menschen ab 18 Jahren.
Aufgabenstellung
Es sollte zu einem Drama-Thriller-Krimi passen. Das Buch beinhaltet knapp 280 Seiten und es endet mit einem Selbstmord am Strand.
Das Buch wird heißen: kuşlar yağmurda. Es ist türkisch und heißt 'die Vögel sind im kalten Regen'.
Es handelt über folgendes: Ein Kind wird entführt - es wird die Organ Mafia beschuldigt am Ende stellt sich heraus das der neue Partner der Mutter das Kind entführt hat. Die Mutter wusste Bescheid. Die Geschichte wird von der Sicht eines Journalisten erzählt. Der Mann der Selbstmord begeht ist der Journalist.
Der Autor ist Kemal Duruöz und soll auch auf dem Cover sein. Hinten auf der Rückseite soll ein Platz für einen Kurztext gelassen werden.
Buchformat ist : 13,5×19,5 cm Hochformat.
Das Design des Covers soll die Trauer wiedergeben.
Tipp: Zb. könnte es ein Mann am Strand alleine widerspiegeln. Wir sind aber offen auch für andere Vorschläge.

```html
<!DOCTYPE html>
<html lang="tr">
<head>
<meta charset="utf-8">
<title>kuşlar yağmurda – Kemal Duruöz</title>
<link rel="stylesheet" href="https://fonts.googleapis.com/css2?family=Alfa+Slab+One&family=Special+Elite&family=Montserrat:wght@500&display=swap">
<style>
  :root {
    --ink-navy: #232c4a;
    --text-dark: #1b1714;
    --sand-cream: #efe6d2;
    --name-beige: #b9a88f;
    --sky-light: #f3efe7;
    --sky-mid: #cfc8bd;
    --sun-glow: #fff8e4;
    --sea-grey: #a49d94;
    --sand-dark: #3b302b;
    --sand-deep: #241c18;
    --label-black: #0b0b0b;
    --panel-white: #f6f7fb;
    --photo-dark: #2a2420;
  }
  * { margin: 0; padding: 0; box-sizing: border-box; }
  html, body { width: 1200px; height: 815px; overflow: hidden; background: #fff; }
  .book-wrap {
    position: relative;
    width: 1200px;
    height: 815px;
    overflow: hidden;
  }
  .beach-scene {
    position: absolute;
    inset: 0;
    background:
      radial-gradient(ellipse 260px 180px at 909px 361px, var(--sun-glow) 0%, rgba(255,248,228,0.6) 40%, rgba(255,248,228,0) 100%),
      linear-gradient(180deg,
        var(--sky-mid) 0%,
        var(--sky-light) 18%,
        #e9e1d3 45%,
        #d8cfc1 54%,
        var(--sea-grey) 56%,
        #cfc6b8 63%,
        #bfb4a6 67%,
        var(--sand-dark) 68%,
        #2f2622 82%,
        var(--sand-deep) 100%);
  }
  .back-blurb {
    position: absolute;
    left: 52px;
    top: 49px;
    width: 494px;
    font-family: "Special Elite", "Courier New", monospace;
    font-size: 13.4px;
    line-height: 19.2px;
    color: var(--text-dark);
    text-align: justify;
    text-align-last: left;
  }
  .author-portrait {
    position: absolute;
    left: 57px;
    top: 560px;
    width: 155px;
    height: 169px;
    background: linear-gradient(90deg, #5a4e44 0%, var(--photo-dark) 14%, #16120f 50%, var(--photo-dark) 86%, #5a4e44 100%);
  }
  .author-caption {
    position: absolute;
    left: 57px;
    top: 744px;
    width: 155px;
    text-align: center;
    font-family: "Alfa Slab One", Georgia, serif;
    font-size: 13px;
    color: var(--name-beige);
    white-space: nowrap;
  }
  .blurb-panel {
    position: absolute;
    left: 347px;
    top: 640px;
    width: 191px;
    height: 117px;
    background: var(--panel-white);
  }
  .spine-title {
    position: absolute;
    left: 578px;
    top: 64px;
    height: 340px;
    writing-mode: vertical-rl;
    font-family: "Alfa Slab One", Georgia, serif;
    font-size: 33px;
    color: var(--ink-navy);
    white-space: nowrap;
  }
  .spine-author {
    position: absolute;
    left: 592px;
    top: 568px;
    writing-mode: vertical-rl;
    font-family: "Alfa Slab One", Georgia, serif;
    font-size: 17px;
    letter-spacing: 1px;
    color: var(--sand-cream);
    white-space: nowrap;
  }
  .front-title {
    position: absolute;
    left: 702px;
    top: 48px;
    width: 432px;
    font-family: "Alfa Slab One", Georgia, serif;
    color: var(--ink-navy);
    white-space: nowrap;
  }
  .front-title .line-one {
    display: block;
    font-size: 112px;
    line-height: 136px;
    letter-spacing: 10px;
  }
  .front-title .line-two {
    display: block;
    font-size: 70px;
    line-height: 84px;
    letter-spacing: 1px;
  }
  .front-author {
    position: absolute;
    left: 730px;
    top: 706px;
    width: 360px;
    text-align: center;
    font-family: "Alfa Slab One", Georgia, serif;
    font-size: 36px;
    letter-spacing: 1px;
    color: var(--sand-cream);
    white-space: nowrap;
  }
  .genre-label {
    position: absolute;
    left: 847px;
    top: 759px;
    width: 123px;
    height: 56px;
    background: var(--label-black);
    color: #fff;
    font-family: "Montserrat", Arial, sans-serif;
    font-weight: 500;
    font-size: 25px;
    line-height: 56px;
    text-align: center;
    letter-spacing: 1px;
  }
</style>
</head>
<body>
<main class="book-wrap">
  <div class="beach-scene" role="img" aria-label="Photograph of a lone man in silhouette standing on a wet beach at sunset, a farewell word written in the sand beside a dropped teddy bear"></div>

  <p class="back-blurb">
    Bir ömür böyle nasıl geçecek?<br>
    Yaşamak ne zormuş ıskalanan hayatta!<br>
    Büyük yanılgılar ve yenilgiler yasamış bir insanım artık<br>
    Hayat elime vermiş yanlış bir pusula, hangi yöne gitsem;<br>
    öteki hüzünler ülkesi.Ne yana yürüsem; acımı çoğaltan dikenli yollar<br>
    Yoksa; bana mükafat olarak, son düzlükte ölüm mü var!<br>
    Dalgın bir yolcu gibi o düzlüğe doğru yürüyorum<br>
    Düğmesi olmayan beyaz gömleğimin mevsimindeyim,<br>
    avluda beklettiğiniz yolcu benim<br>
    Soğudu yaşam; zamanın dışında, bir boşluğun içindeyim<br>
    Başka insanların acılarını kendi yüreğimde hissetmek ne yorucu bir duygu<br>
    Oysa; ben kendimi ararken başkalarının acılarına ortak olmuşum<br>
    Adeta dünyada olup biten, tüm kötü şeylerin sorumlusu benmişim gibi,<br>
    kendimi bundan sorumlu tutuyorum.Hayat kör bir kuyu, hiçbir şey kalıcı değil,<br>
    hep aynı kalmıyor ki yakın duygular, taze bir karanfil de ölebiliyor avuçlarında,<br>
    bir boşlukta sallandırıyorsun yüreğini, yarından önce gidenleri özlüyorsun.<br>
    Hayat merdivenleri çürük bir tahta gibidi. Her an düşebiliyorsun bir karanlığa<br>
    İnsan kendini öldürüyor işte, yaşamak için umut kalmayınca..
  </p>

  <div class="author-portrait" role="img" aria-label="Portrait photograph of the author leaning in a wooden window frame"></div>
  <p class="author-caption">KEMAL DURUÖZ</p>

  <div class="blurb-panel"></div>

  <p class="spine-title">kuşlar yağmurda</p>
  <p class="spine-author">KEMAL DURUÖZ</p>

  <h1 class="front-title">
    <span class="line-one">kuşlar</span>
    <span class="line-two">yağmurda</span>
  </h1>

  <p class="front-author">KEMAL DURUÖZ</p>
  <p class="genre-label">ROMAN</p>
</main>
</body>
</html>
```